依頼詳細
作成している原稿があるので別途添付いたします。
記載項目
作成原稿にすべて入れています。
サイズ
A4
ページ数
片面
希望イメージ
シンプル 複雑
単色 カラフル
暗い 明るい
日常 高級
遊び心 厳粛
未来的 伝統的
女性的 男性的
希望する色
無彩色系、無彩色系ですが明るめの色もあれば見たいです
納品ファイル
• イラストレーター形式 (.ai)
• PNG形式 (.png)
補足説明

```html
<!DOCTYPE html>
<html lang="ja">
<head>
<meta charset="utf-8">
<title>ご縁結び学舎 群馬校 開校プレ講演会</title>
<link href="https://fonts.googleapis.com/css2?family=Shippori+Mincho+B1:wght@600;800&family=Noto+Sans+JP:wght@400;700;900&display=swap" rel="stylesheet">
<style>
:root{
  --ink:#2b2a2a;
  --pink:#e8558f;
  --pink-soft:#f7c9da;
  --pink-pale:#fdeef3;
  --red:#d2262f;
  --gold:#c9a24a;
  --teal:#1f4f5a;
  --grey:#6d6d6d;
  --paper:#ffffff;
}
*{margin:0;padding:0;box-sizing:border-box}
html,body{width:846px;height:1200px;overflow:hidden;background:var(--paper)}
.poster{position:relative;width:846px;height:1200px;overflow:hidden;background:var(--paper);font-family:"Noto Sans JP",sans-serif;color:var(--ink)}
.abs{position:absolute}
.flowers{left:110px;top:250px;width:300px;height:420px;border-radius:50%;background:radial-gradient(circle at 50% 50%,#f6b8cd 0%,#fbdbe6 45%,rgba(255,255,255,0) 72%)}
.flowers-top{left:250px;top:40px;width:380px;height:170px;border-radius:50%;background:radial-gradient(ellipse at 50% 50%,#fbd3e0 0%,rgba(255,255,255,0) 70%)}
.knot{left:230px;top:200px;width:420px;height:200px;border-radius:50%;background:radial-gradient(ellipse at 50% 50%,rgba(210,38,47,.28) 0%,rgba(201,162,74,.18) 45%,rgba(255,255,255,0) 72%)}
.rules{left:28px;top:40px;height:330px;writing-mode:vertical-rl;font-size:15px;line-height:26px;font-weight:700}
.rules .lead{font-size:12px;font-weight:400;color:var(--grey)}
.rules .rule-title{display:inline-block;border:2px solid var(--ink);padding:6px 2px;margin:0 6px;font-size:19px;font-weight:900}
.ema{right:40px;top:30px;width:120px;height:230px;background:var(--paper);border:3px solid var(--pink-soft);clip-path:polygon(50% 0,100% 18%,100% 100%,0 100%,0 18%)}
.ema-text{right:62px;top:72px;writing-mode:vertical-rl;font-family:"Shippori Mincho B1",serif;font-weight:800;color:var(--red);font-size:19px;line-height:26px}
.title{font-family:"Shippori Mincho B1",serif;font-weight:800;writing-mode:vertical-rl;color:var(--ink);letter-spacing:2px}
.title-a{left:436px;top:90px;font-size:50px}
.title-b{left:356px;top:120px;font-size:50px}
.title .en{color:var(--pink);font-size:76px}
.photo{left:500px;top:320px;width:346px;height:410px;background:linear-gradient(160deg,#d9d4cf 0%,#8e8277 55%,#3e3631 100%)}
.date{left:150px;top:690px}
.year{font-size:24px;font-weight:900;display:block}
.day{font-size:78px;font-weight:900;line-height:1;letter-spacing:-1px}
.day small{font-size:34px}
.time{left:150px;top:792px;font-size:15px;font-weight:700}
.venue{left:150px;top:818px;display:flex;align-items:center;gap:10px;font-size:22px;font-weight:900}
.venue .tag{background:var(--pink);color:#fff;font-size:14px;padding:2px 8px}
.address{left:150px;top:848px;font-size:11px;color:var(--grey);line-height:16px}
.speaker{left:620px;top:815px;font-family:"Shippori Mincho B1",serif;font-weight:800;font-size:30px}
.speaker span{font-size:15px;margin-right:6px}
.contact{left:28px;top:880px;color:var(--teal)}
.contact small{font-size:13px;display:block;font-weight:700}
.contact strong{font-size:44px;font-weight:900;letter-spacing:1px}
.schedule{left:22px;top:962px;width:470px;height:220px;border:2px solid var(--pink);background:var(--pink-pale)}
.schedule h2{background:var(--pink);color:#fff;font-size:17px;padding:6px 12px;font-weight:900}
.schedule ul{list-style:none;padding:10px 14px;font-size:13px;line-height:27px}
.schedule li::before{content:"";display:inline-block;width:8px;height:8px;background:var(--pink);border-radius:50%;margin-right:8px}
.info{left:510px;top:962px;width:316px;font-size:11px;line-height:17px;color:var(--ink)}
.info h3{display:inline-block;background:var(--ink);color:#fff;font-size:11px;padding:1px 6px;margin:4px 0 2px}
.map{left:676px;top:1086px;width:150px;height:96px;background:linear-gradient(135deg,#eeeeee,#d6d6d6);border:1px solid #bbb}
</style>
</head>
<body>
<div class="poster">
  <div class="abs flowers-top" role="img" aria-label="淡いピンクの花の装飾"></div>
  <div class="abs flowers" role="img" aria-label="ピンクのガーベラの花の装飾"></div>
  <div class="abs knot" role="img" aria-label="紅白と金の水引の結び飾り"></div>

  <div class="abs rules">
    <span class="lead">今日、あなたのメッセージになります</span>
    <span class="rule-title">「4つの鉄板ルール」</span><br>
    1 自分から話しかけること！<br>
    2 約束は必ず守ること！<br>
    3 出来ない言い訳をしない！<br>
    4 そのうちを今日にすること！
  </div>

  <div class="abs ema"></div>
  <div class="abs ema-text">ご縁結び学舎<br>群馬校<br>開校プレ講演会</div>

  <div class="abs title title-a">出会いこそ宝である</div>
  <div class="abs title title-b">人の<span class="en">ご縁</span>ででっかく生きろ</div>

  <div class="abs photo" role="img" aria-label="マイクを持って話す講師の写真"></div>

  <div class="abs date"><span class="year">2020年</span><span class="day">7.11<small>(土)</small></span></div>
  <div class="abs time">開演／18:30（開場／18:00）</div>
  <div class="abs venue"><span class="tag">会場</span>緑ヶ丘シティホール</div>
  <div class="abs address">高崎市若葉町12-3 TEL.027-300-0000<br>主催：ご縁結び学舎群馬校実行委員会</div>

  <div class="abs speaker"><span>講師</span>森川 達也</div>

  <div class="abs contact"><small>（お問い合わせ）ミナトカンパニー</small><strong>TEL.0596-00-1234</strong></div>

  <section class="abs schedule">
    <h2>ご縁結び学舎 群馬校1期 開催予定</h2>
    <ul>
      <li>第1講 8/10(月)「人に会うと人生は変わる」森川達也</li>
      <li>第2講 9/13(日)「まず自分から動こう」講師未定</li>
      <li>第3講 10/11(日)「感謝を伝える力」講師未定</li>
      <li>第4講 11/8(日)「言葉で縁をつなぐ」講師未定</li>
      <li>第5講 12/13(日)「仕事とご縁の話」講師未定</li>
      <li>第6講 1/10(日)「自分の道を歩む」森川達也</li>
    </ul>
  </section>

  <div class="abs info">
    <h3>チケット</h3><br>一般 3,000円（当日3,500円）学生 1,500円<br>
    <h3>お申し込み方法</h3><br>お電話またはメールにてお申し込みください。<br>info@minato-co.example<br>
    <h3>アクセス</h3><br>高崎駅西口より徒歩10分<br>駐車場に限りがあります。
  </div>
  <div class="abs map" role="img" aria-label="会場周辺の地図"></div>
</div>
</body>
</html>
```